Foldable creative restaurant menu

We require foldable restaurant menu to be placed on the each table, want it to look creative and modern with pages representing pictures of the dish not all dishes but few to represent what we do.Please get creative make sure its different, the colour should represent classy restaurant, not cheap and fast. The shape of the menu can be difference creative words must be easy to read and the logo must be in the menu here and there briefly.

Target Market(s)

Restaurant customers

Industry/Entity Type

Health And Wellness

Colors

Designer to choose colors to be used in the design.

Requirements
Must have
• foldable, must have good dish presentation pictures and must look modern and classy
Nice to have
• funky design and creative can be not just square foldable but can be interesting shape of menu.
Should not have
• boring plain spaces
• small writing
• dark pictures

```html
<!DOCTYPE html>
<html lang="en">
<head>
<meta charset="utf-8">
<title>Lumora Restaurant – Drinks Menu</title>
<link rel="stylesheet" href="https://fonts.googleapis.com/css2?family=Montserrat:wght@200;300;600;700&family=Archivo:wght@400;600;700&display=swap">
<style>
:root{
  --ink:#1b1b1b;
  --frame:#3a3a3a;
  --paper:#ffffff;
  --muted:#444;
}
*{box-sizing:border-box;margin:0;padding:0}
html,body{width:1200px;height:779px;overflow:hidden;background:var(--paper)}
body{position:relative;font-family:'Archivo',Arial,sans-serif;color:var(--ink)}
.panel{position:absolute;width:367px;height:175px;border:1px solid var(--frame);background:var(--paper);overflow:hidden}
.c1{left:22px}.c2{left:418px}.c3{left:814px}
.r1{top:21px}.r2{top:211px}.r3{top:400px}.r4{top:589px}
.panel-photo{position:absolute;top:0;right:0;width:45%;height:100%}
.panel-copy{position:absolute;left:26px;top:15px;width:48%;font-size:4.4px;line-height:1.35}
.panel-title{font-family:'Montserrat',Arial,sans-serif;font-weight:700;font-size:7.6px;letter-spacing:1.3px;margin-bottom:11px}
.size-line{margin-bottom:6px;font-size:4.3px}
.item{margin-bottom:6px}
.item-name{font-weight:700;font-size:5.6px;line-height:1.3}
.item-desc{font-size:4.2px;color:var(--muted)}
.addons{position:absolute;left:26px;bottom:10px;font-size:4.2px}
.price-row{display:flex;justify-content:space-between;align-items:baseline;font-weight:700;font-size:5.6px;margin-bottom:8px}
.price-row.lead{margin-bottom:1px}
.sub{font-size:4.2px;font-weight:400;color:var(--muted);margin-bottom:6px}
.group-head{font-weight:700;font-size:6.2px;margin-top:5px}
.cols{display:flex;gap:14px}
.cols ul{list-style:none}
.cols li{display:flex;justify-content:space-between;width:76px;font-size:4.2px;line-height:1.35}
/* wine price tables */
.price-table{font-size:4.2px;line-height:1.4;margin-bottom:6px}
.price-table .row{display:grid;grid-template-columns:90px 28px 28px 28px;align-items:baseline;white-space:nowrap}
.price-table.bubbly .row{grid-template-columns:100px 50px 30px}
.price-table .head{margin-bottom:1px}
.price-table .label{font-weight:700;font-size:5.4px}
.price-table .label small{font-weight:400;font-size:4.2px}
.price-table .special{margin-top:4px}
/* cover */
.cover-side{position:absolute;top:50%;left:36px;transform:translate(-50%,-50%) rotate(-90deg);font-family:'Montserrat',Arial,sans-serif;font-weight:700;font-size:10.5px;letter-spacing:2.3px;white-space:nowrap}
.cover-name{position:absolute;left:54px;top:52px;font-family:'Montserrat',Arial,sans-serif;font-weight:200;font-size:34px;letter-spacing:2px}
.cover-sub{position:absolute;left:55px;top:102px;font-family:'Montserrat',Arial,sans-serif;font-weight:300;font-size:15px;letter-spacing:4.2px}
.photo-latte{background:radial-gradient(circle at 45% 42%,#c9a27a 0,#9b6a45 30%,#6d4528 45%,#e9e3d8 62%,#cfc7bb 100%)}
.photo-cocoa{background:radial-gradient(circle at 60% 60%,#8d6552 0,#b48877 30%,#efe0dc 55%,#f7eeeb 100%)}
.photo-tea{background:radial-gradient(circle at 45% 30%,#d8a646 0,#e9dcc2 18%,#f3f2ef 40%,#e8e8e6 100%)}
.photo-iced{background:linear-gradient(160deg,#6b5a4c 0,#8a7666 35%,#b9c0c6 65%,#6e7377 100%)}
.photo-smoothie{background:linear-gradient(150deg,#6b5a49 0,#c98fb1 40%,#e3b2cf 65%,#3c3550 100%)}
.photo-cola{background:radial-gradient(circle at 55% 55%,#5a2f12 0,#3b1e0c 40%,#c9c2b8 75%,#f1eee9 100%)}
.photo-beer{background:radial-gradient(ellipse at 55% 55%,#e3a526 0,#a86a12 45%,#1a1208 80%,#000 100%)}
.photo-wine{background:linear-gradient(140deg,#efe4c9 0,#d9c89d 35%,#4f7d2e 60%,#6b8f3a 80%,#c9b184 100%)}
.photo-bubbly{background:radial-gradient(circle at 40% 55%,#efe6b8 0,#c7c08a 25%,#4a6aa8 60%,#2e4272 100%)}
</style>
</head>
<body>

<section class="panel c1 r1 cover">
  <div class="cover-side">DRINKS MENU</div>
  <div class="cover-name">Lumora</div>
  <div class="cover-sub">RESTAURANT</div>
</section>

<section class="panel c2 r1">
  <div class="panel-copy">
    <h2 class="panel-title">HOT BEVERAGE</h2>
    <p class="size-line">Cup 3.50 | Mug 4.50 | Takeaway 4.90/3.90 (S)</p>
    <div class="item"><p class="item-name">Espresso</p><p class="item-desc">Coffee brewed by forcing a shot of nearly boiling water under pressure through finely ground coffee beans</p></div>
    <div class="item"><p class="item-name">Americano</p><p class="item-desc">Shots of espresso with hot water flavour and body of an American-style drip coffee</p></div>
    <div class="item"><p class="item-name">Flat White</p><p class="item-desc">Pouring steamed milk consisting of small, fine bubbles with a glossy or velvety consistency over a shot of espresso</p></div>
    <div class="item"><p class="item-name">Latte</p><p class="item-desc">Freshly steamed milk without foam served with a shot of espresso coffee</p></div>
    <div class="item"><p class="item-name">Piccolo Latte</p></div>
  </div>
  <p class="addons">Decaf 0.60 | Vanilla 0.60 | Hazelnut 0.60 | Caramel 0.60 | Chai 0.60</p>
  <div class="panel-photo photo-latte" role="img" aria-label="Latte with leaf art in a cup on a saucer with a spoon"></div>
</section>

<section class="panel c3 r1">
  <div class="panel-copy">
    <h2 class="panel-title">HOT BEVERAGE</h2>
    <p class="size-line">Cup 3.50 | Mug 4.50 | Takeaway 4.90/3.90 (S)</p>
    <div class="item"><p class="item-name">Chai Latte</p><p class="item-desc">Chai Tea Concentrate infusion Of Black Tea, Cardamom, Black Pepper, Ginger, Cinnamon, Cloves, Natural Flavours, Star Anise, Sugar, Honey, Ginger Juice, Natural Flavours, Vanilla, and Citric Acid served as latte</p></div>
    <div class="item"><p class="item-name">Cappuccino</p><p class="item-desc">Steamed foamed velvety milk poured over shot of coffee freshly ground beans producing essence, finished by topping with foam and a sprinkle of chocolate powder</p></div>
    <div class="item"><p class="item-name">Macchiato</p><p class="item-desc">A touch of steamed foamed milk added to a double shot of coffee extract</p></div>
    <div class="item"><p class="item-name">Hot Chocolate</p><p class="item-desc">Sweet chocolate drink made with steamed milk</p></div>
  </div>
  <p class="addons">Decaf 0.60 | Vanilla 0.60 | Hazelnut 0.60 | Caramel 0.60 | Chai 0.60</p>
  <div class="panel-photo photo-cocoa" role="img" aria-label="Glass mug of hot chocolate with chocolate pieces"></div>
</section>

<section class="panel c1 r2">
  <div class="panel-copy">
    <h2 class="panel-title">HOT BEVERAGE</h2>
    <p class="size-line" style="margin-bottom:2px">Cup 3.50 | Mug 4.50 | Takeaway 5.20</p>
    <div class="item"><p class="item-name">Mochacchino</p><p class="item-desc">Combination of chocolate syrup and a shot of espresso, topped with steamed milk and a layer of micro-foam and a sprinkle of chocolate powder</p></div>
    <p class="size-line" style="margin-bottom:2px">Cup 2.50 | Mug 3.50 | Takeaway 4.00</p>
    <div class="item"><p class="item-name">Babyccino</p><p class="item-desc">Warm milk in a small cup and topped with milk froth and chocolate powder. No espresso coffee essence is added.</p></div>
    <div class="price-row lead" style="width:168px;margin-top:10px"><span>Hot Tea</span><span>4.50</span></div>
    <p class="sub">English breakfast | Earl Grey | Sencha | Chamomile |<br>Mint | Lemongrass | Chai</p>
  </div>
  <p class="addons">Decaf 0.60 | Vanilla 0.60 | Hazelnut 0.60 | Caramel 0.60 | Chai 0.60</p>
  <div class="panel-photo photo-tea" role="img" aria-label="Cup of tea and white teapot with herbs"></div>
</section>

<section class="panel c2 r2">
  <div class="panel-copy" style="width:170px">
    <h2 class="panel-title">CHILLED BEVERAGE</h2>
    <div class="price-row"><span>Iced Long Black</span><span>4.90</span></div>
    <div class="price-row"><span>Iced Latte</span><span>5.90</span></div>
    <div class="price-row"><span>Iced Chocolate</span><span>5.90</span></div>
    <div class="price-row"><span>Iced Mocha</span><span>6.20</span></div>
    <div class="price-row lead"><span>MILKSHAKES</span><span>8.00</span></div>
    <p class="sub">Chocolate, Strawberry, Caramel</p>
    <div class="price-row"><span>THICKSHAKES</span><span>10.00</span></div>
  </div>
  <div class="panel-photo photo-iced" role="img" aria-label="Iced coffee with cream in a glass on a saucer"></div>
</section>

<section class="panel c3 r2">
  <div class="panel-copy" style="width:170px">
    <h2 class="panel-title">SMOOTHIES</h2>
    <div class="price-row lead"><span>ACAI</span><span>9.00</span></div>
    <p class="sub">Choice of:<br>Brazilian Super –<br>Acai puree OR energy, Banana and Almond Milk OR Apple Juice<br><br>Cocoberry Bang –<br>Coconut Flesh, Banana, Frozen mixed berries and Coconut water</p>
    <div class="price-row lead"><span>LEAN &amp; GREEN –</span><span>9.00</span></div>
    <p class="sub">Kale/Spinach, Cucumber, Celery &amp; Banana</p>
    <div class="price-row lead"><span>MANGO –</span><span>8.00</span></div>
    <p class="sub">Mango, Yogurt, Milk &amp; Honey</p>
    <div class="price-row lead"><span>BANANA –</span><span>8.00</span></div>
    <p class="sub">Banana, Yogurt, Milk, Honey &amp; Cinnamon</p>
    <div class="price-row lead"><span>MIXED BERRY –</span><span>8.00</span></div>
    <p class="sub">Mixed Berries, Yogurt, Milk &amp; Honey</p>
    <p class="sub">ADD Protein Powder 2 | Chia Seed 2 | Oats 2</p>
  </div>
  <div class="panel-photo photo-smoothie" role="img" aria-label="Berry smoothies topped with blackberries and mint"></div>
</section>

<section class="panel c1 r3">
  <div class="panel-copy" style="width:170px">
    <h2 class="panel-title">BEVERAGE</h2>
    <div class="price-row lead"><span>SOFT DRINKS</span><span>4.00 (500ml) | 8.00 (Jug)</span></div>
    <p class="sub">Cola, Diet Cola, Zest, Lemon Spark, Soda Water, Raspberry Lemonade,<br>Lemon Lime &amp; Bitters, Lime &amp; Soda, Soda Lime &amp; Bitters</p>
    <p class="group-head">MINERAL WATER</p>
    <div class="price-row lead"><span class="sub" style="margin:0">Mount Ferris Sparkling (Lightly/ Lemon/ Lime/ Raspberry) 450ml</span><span>4.00</span></div>
    <div class="price-row lead"><span class="sub" style="margin:0">Mount Ferris Still 600ml</span><span>3.00</span></div>
    <div class="price-row"><span class="sub" style="margin:0">Palmo Coconut water 330ml</span><span>4.00</span></div>
    <div class="price-row lead"><span>FRESH SQUEEZED JUICES</span><span>4.00 (250ml) | 8.00 (500ml)</span></div>
    <p class="sub">Orange Juice</p>
  </div>
  <div class="panel-photo photo-cola" role="img" aria-label="Glass of cola with ice cubes"></div>
</section>

<section class="panel c2 r3">
  <div class="panel-copy" style="width:190px">
    <h2 class="panel-title" style="margin-bottom:6px">BEER &amp; CIDER</h2>
    <p class="group-head" style="margin-top:0">BOTTLED BEER</p>
    <div class="cols">
      <ul>
        <li><span>Quarry Gold</span><span>6.00</span></li>
        <li><span>Kelburn Mid</span><span>6.00</span></li>
        <li><span>Cobalt Lager</span><span>6.00</span></li>
        <li><span>Quarry Summer</span><span>6.00</span></li>
        <li><span>Kelburn Draught</span><span>6.00</span></li>
        <li><span>Regent Lager</span><span>6.50</span></li>
        <li><span>Marrow Pale ale</span><span>6.00</span></li>
        <li><span>Kelburn Dry</span><span>6.00</span></li>
        <li><span>Pale Sun Blonde</span><span>6.00</span></li>
        <li><span>Wendra Pale ale</span><span>6.00</span></li>
      </ul>
      <ul>
        <li><span>Wendra Golden</span><span>6.00</span></li>
        <li><span>Bramwell</span><span>6.00</span></li>
        <li><span>Toller New</span><span>6.00</span></li>
        <li><span>Halden super dry</span><span>6.00</span></li>
        <li><span>Riverfall light</span><span>6.00</span></li>
        <li><span>Toller Old</span><span>6.00</span></li>
        <li><span>Halden Light</span><span>6.00</span></li>
        <li><span>Fortlake</span><span>6.00</span></li>
        <li><span>Toller Extra Dry</span><span>6.00</span></li>
        <li><span>Solana</span><span>6.00</span></li>
      </ul>
    </div>
    <p class="group-head">PREMIX</p>
    <div class="cols">
      <ul>
        <li><span>Jed Barrow &amp; Cola</span><span>7.50</span></li>
        <li><span>Jonah Dale &amp; Cola</span><span>7.50</span></li>
        <li><span>Rustwood</span><span>7.50</span></li>
      </ul>
      <ul>
        <li><span>Northern Cask Cola</span><span>7.50</span></li>
        <li><span>Northern Cask Dry</span><span>7.50</span></li>
      </ul>
    </div>
    <p class="group-head">BOTTLED CIDER</p>
    <div class="cols">
      <ul>
        <li><span>Orchardby Apple</span><span>7.50</span></li>
        <li><span>Orchardby Pear</span><span>7.50</span></li>
      </ul>
      <ul>
        <li><span>Fjordling Passionfruit</span><span>7.50</span></li>
        <li><span>Fjordling Strawberry &amp; Lime</span><span>7.50</span></li>
      </ul>
    </div>
  </div>
  <div class="panel-photo photo-beer" role="img" aria-label="Frosted mug of golden beer on black"></div>
</section>

<section class="panel c3 r3">
  <div class="panel-copy" style="width:190px">
    <h2 class="panel-title">WINE</h2>
    <div class="price-table">
      <div class="row head"><span class="label">RED WINE <small>(house collection)</small></span><span>Glass 150ml</span><span>Glass 250ml</span><span>Bottle 750ml</span></div>
      <div class="row"><span>Shiraz</span><span>7.00</span><span>9.00</span><span>29.00</span></div>
      <div class="row"><span>Merlot</span><span>7.00</span><span>9.00</span><span>29.00</span></div>
      <div class="row"><span>Cabernet Sauvignon</span><span>7.00</span><span>9.00</span><span>29.00</span></div>
      <div class="row special"><span>SPECIAL</span></div>
      <div class="row"><span>Shiraz (small bottle 187 ml)</span><span>8.00</span></div>
    </div>
    <div class="price-table">
      <div class="row head"><span class="label">WHITE WINE <small>(house collection)</small></span><span>Glass 150ml</span><span>Glass 250ml</span><span>Bottle 750ml</span></div>
      <div class="row"><span>Moscato</span><span>7.00</span><span>9.00</span><span>29.00</span></div>
      <div class="row"><span>Sauvignon Blanc</span><span>7.00</span><span>9.00</span><span>29.00</span></div>
      <div class="row special"><span>SPECIAL</span></div>
      <div class="row"><span>Sauvignon Blanc (small bottle 187 ml)</span><span>8.00</span></div>
    </div>
    <div class="price-table">
      <div class="row head"><span class="label">ROSE WINE</span><span>Glass 150ml</span><span>Glass 250ml</span><span>Bottle 750ml</span></div>
      <div class="row"><span>Merlot Rose</span><span>7.00</span><span>9.00</span><span>29.00</span></div>
      <div class="row special"><span>SPECIAL</span></div>
      <div class="row"><span>Pink Moscato (small bottle 187 ml)</span><span>8.00</span></div>
    </div>
  </div>
  <div class="panel-photo photo-wine" role="img" aria-label="Glasses of white and red wine with green and dark grapes"></div>
</section>

<section class="panel c1 r4">
  <div class="panel-copy" style="width:190px">
    <h2 class="panel-title">CHAMPAGNE</h2>
    <div class="price-table bubbly">
      <div class="row head"><span class="label">CHAMPAGNE <small>(sparkling collection)</small></span><span>Glass 150ml</span><span>Bottle 750ml</span></div>
      <div class="row"><span>Sparkling Brut</span><span></span><span>30.00</span></div>
      <div class="row special"><span>SPECIAL</span></div>
      <div class="row"><span>Pinot Noir Chardonnay (small bottle 200 ml)</span><span>8.5</span></div>
    </div>
  </div>
  <div class="panel-photo photo-bubbly" role="img" aria-label="Two glasses of sparkling wine with blue flowers behind"></div>
</section>

</body>
</html>
```